Our swimming pool service needs your help with letterhead

Letterhead for small swimming pool service- We would like a professional look with a creative layout- must be compatible with QuickBooks forms (sample attached)
No more than 2 colors in graphics

Target Market(s)

Homeowners/ Contractors

Font styles to use
Sans Serif

Colors
33a6d7
85cae6

Requirements
Must have
• Logo (file attached)
• Compatible with QuickBooks (sample attached)
• Mailing address- P.O. Box 52, Harlow Bend NY 11603
• phone- (631) 582-9016
• email- marcotrentpools@fernmail.test
• Licensed & Insured
Nice to have
• Small slogan- Examples:Family owned and operated for 25 years, 25 years of trusted service
• Creative layout
Should not have
• Blue color must be same as blue in our logo
• No thick lines of color
• No design in middle of page

```html
<!DOCTYPE html>
<html lang="en">
<head>
<meta charset="utf-8">
<title>Marco Trent Pool Service – Letterhead</title>
<link rel="stylesheet" href="https://fonts.googleapis.com/css2?family=Poppins:wght@400;500;600&display=swap">
<style>
  :root {
    --navy: #233a5c;
    --sky: #6aaee0;
    --ink: #555a60;
    --paper: #ffffff;
    --rule: #d6d8db;
  }
  * { margin: 0; padding: 0; box-sizing: border-box; }
  html, body { width: 906px; height: 1200px; overflow: hidden; background: var(--paper); }
  body { font-family: "Poppins", sans-serif; }
  .letterhead { position: relative; width: 906px; height: 1200px; background: var(--paper); }

  .tagline-bar {
    height: 48px; background: var(--navy);
    border-bottom: 2px solid var(--sky);
    display: flex; align-items: center; justify-content: center;
    color: #fff; font-size: 16.5px; font-weight: 500; letter-spacing: 0.1px;
  }
  .tagline-bar .divider { width: 1px; height: 22px; background: #fff; margin: 0 12px; }

  .brand {
    position: absolute; left: 30px; top: 94px;
    display: flex; align-items: center; gap: 10px;
  }
  .brand-dot { width: 28px; height: 28px; border-radius: 50%; background: var(--sky); flex: none; }
  .brand-name { font-size: 22px; font-weight: 600; color: var(--navy); letter-spacing: 0.2px; white-space: nowrap; }

  .contact {
    position: absolute; left: 548px; top: 71px; height: 90px;
    border-left: 1px solid var(--rule); padding-left: 24px;
    display: flex; flex-direction: column; justify-content: space-between;
    font-style: normal;
  }
  .contact-row { display: flex; align-items: center; gap: 11px; font-size: 17px; color: var(--ink); line-height: 22px; white-space: nowrap; }
  .contact-row svg { width: 16px; height: 16px; fill: var(--navy); flex: none; }

  .footer-band {
    position: absolute; left: 0; bottom: 0; width: 906px; height: 67px;
    background: linear-gradient(180deg, var(--sky) 0%, var(--navy) 60%);
  }
</style>
</head>
<body>
<main class="letterhead">
  <header class="tagline-bar">
    <span>Licensed &amp; Insured</span>
    <span class="divider"></span>
    <span>Family Owned And Operated For 25 Years</span>
  </header>

  <div class="brand">
    <span class="brand-dot"></span>
    <span class="brand-name">Marco Trent Pool Service</span>
  </div>

  <address class="contact">
    <div class="contact-row">
      <svg viewBox="0 0 16 16" aria-hidden="true"><rect x="4" y="1" width="8" height="14" rx="1.2"/><rect x="5.5" y="3" width="5" height="4" fill="#fff"/><rect x="5.5" y="8.5" width="1.3" height="1.2" fill="#fff"/><rect x="7.4" y="8.5" width="1.3" height="1.2" fill="#fff"/><rect x="9.2" y="8.5" width="1.3" height="1.2" fill="#fff"/><rect x="5.5" y="10.8" width="1.3" height="1.2" fill="#fff"/><rect x="7.4" y="10.8" width="1.3" height="1.2" fill="#fff"/><rect x="9.2" y="10.8" width="1.3" height="1.2" fill="#fff"/></svg>
      <span>(631) 582-9016</span>
    </div>
    <div class="contact-row">
      <svg viewBox="0 0 16 16" aria-hidden="true"><path d="M1 4h14v9H1z"/><path d="M1 4l7 5 7-5" fill="none" stroke="#fff" stroke-width="1.3"/></svg>
      <span>marcotrentpools@fernmail.test</span>
    </div>
    <div class="contact-row">
      <svg viewBox="0 0 16 16" aria-hidden="true"><path d="M8 1a4.6 4.6 0 0 0-4.6 4.6C3.4 9.2 8 15 8 15s4.6-5.8 4.6-9.4A4.6 4.6 0 0 0 8 1zm0 6.4a1.8 1.8 0 1 1 0-3.6 1.8 1.8 0 0 1 0 3.6z"/></svg>
      <span>P.O. Box 52, Harlow Bend NY 11603</span>
    </div>
  </address>

  <div class="footer-band" role="img" aria-label="Decorative water wave band in sky blue and navy"></div>
</main>
</body>
</html>
```